Valmuna - Plant extraction for human use

Valmuna is a plant extraction based on long pepper containing a high concentration of piperlongumine. Piperlongumine has mainly anti-cancer properties, shown in many animal studies (200). It has as well shown to inhibit dementia and bone inflammation (in animal studies). We are the first to offer this extract for the European market. Because the product will be sold under a ‘plant extraction’ legislation, we cannot make any claims about the medical properties of the extract. I need a design for the packaging (blister pack) in a category for life enhancing medicine with no connotation of cancer for the European market in a first phase. We target people from 35-75 years old. For the younger group of people, we would propose (without saying) to use our product for chemoprevention against cancer. For those patients which have been diagnosed with cancer, we would propose to use it in conjunction with chemo-radio or immunotherapy (without saying).
Target Market(s)
Europe
Look and feel

```html
<!DOCTYPE html>
<html lang="en">
<head>
<meta charset="utf-8">
<title>Valmuna – carton dieline</title>
<link href="https://fonts.googleapis.com/css2?family=Open+Sans:wght@400;600;700&family=Roboto:wght@700&family=Roboto+Condensed:wght@700&display=swap" rel="stylesheet">
<style>
  :root{
    --stage:#333333;
    --paper:#ffffff;
    --brand-blue:#0a42ff;
    --lime:#9dff00;
    --ink:#1b2fa8;
    --on-blue:#ffffff;
  }
  html,body{margin:0;padding:0;width:1200px;height:1139px;overflow:hidden;background:var(--stage);}
  .dieline{display:block;width:1200px;height:1139px;}
  .paper{fill:var(--paper);}
  .blue{fill:var(--brand-blue);}
  .lime{fill:var(--lime);}
  .body-text{font-family:"Open Sans",sans-serif;}
  .on-blue{fill:var(--on-blue);}
  .ink{fill:var(--ink);}
  .brand{font-family:"Roboto",sans-serif;font-weight:700;fill:var(--brand-blue);}
  .condensed{font-family:"Roboto Condensed",sans-serif;font-weight:700;fill:var(--ink);font-size:13.5px;letter-spacing:-0.3px;}
  .line-ink{fill:none;stroke:var(--ink);stroke-width:1.6;}
  .line-white{fill:none;stroke:var(--on-blue);stroke-width:2;}
  .symbol-digit{font-family:"Open Sans",sans-serif;font-weight:700;font-size:14px;}
</style>
</head>
<body>
<svg class="dieline" viewBox="0 0 1702 1616" xmlns="http://www.w3.org/2000/svg">
  <defs>
    <g id="front-graphics">
      <polygon class="lime" points="880,0 1269,0 1269,430 728,430 798,233 380,233 380,212 808,212"/>
      <polygon class="blue" points="902,0 940,0 783,430 746,430"/>
      <rect class="blue" x="466" y="55" width="34" height="49"/>
      <circle class="lime" cx="524" cy="334" r="54"/>
      <!-- sterile badge -->
      <rect class="line-ink" x="1026" y="50" width="97" height="31"/>
      <line class="line-ink" x1="1099" y1="50" x2="1099" y2="81"/>
      <line class="line-ink" x1="1111" y1="56" x2="1111" y2="70"/>
      <circle class="ink" cx="1111" cy="72" r="3"/>
      <!-- warning triangle -->
      <polygon class="line-ink" points="1160,343 1174,368 1146,368"/>
      <line class="line-ink" x1="1160" y1="351" x2="1160" y2="361"/>
      <!-- single use symbol -->
      <circle class="line-ink" cx="1063" cy="385" r="12.5"/>
      <text class="symbol-digit ink" x="1063" y="390" text-anchor="middle">2</text>
      <line class="line-ink" x1="1054" y1="376" x2="1072" y2="394"/>
    </g>
  </defs>

  <!-- flaps and panels -->
  <polygon class="paper" points="243,270 348,243 379,243 379,380 243,372"/>
  <polygon class="paper" points="1269,243 1300,243 1406,270 1406,372 1269,380"/>
  <rect class="paper" x="170" y="380" width="1309" height="430" rx="25"/>
  <polygon class="paper" points="243,818 379,810 379,946 348,946 243,920"/>
  <polygon class="paper" points="1269,810 1269,946 1300,946 1406,920 1406,818"/>
  <rect class="paper" x="379" y="946" width="890" height="431"/>
  <polygon class="paper" points="379,1377 1269,1377 1248,1462 401,1462"/>

  <!-- top band -->
  <rect class="blue" x="379" y="243" width="890" height="137"/>
  <g class="body-text on-blue">
    <text x="473" y="277" font-size="12" font-weight="700">COMPOSITION:</text>
    <text x="473" y="299" font-size="12.5" font-weight="700">Each ml contains Sodium Hyaluronate BP14mg</text>
    <text x="473" y="315" font-size="12.5" font-weight="700">in a sterile isotonic vehicle q.s.</text>
    <text x="473" y="351" font-size="18" font-weight="600" letter-spacing="0.5">SINGLE USE ONLY</text>
    <g font-size="12">
      <text x="962" y="277">Store between 2℃ to 8℃ .</text>
      <text x="962" y="293">Protect from light and freezing.</text>
      <text x="962" y="309">Bring to room temperature prior to use.</text>
      <text x="962" y="325">Do not reuse.</text>
      <text x="962" y="341">Do not use if floating particles are found.</text>
      <text x="962" y="357">Dose: As directed by the Physician.</text>
    </g>
  </g>
  <circle class="line-white" cx="662" cy="345" r="11"/>
  <text class="symbol-digit on-blue" x="662" y="350" text-anchor="middle">2</text>
  <line class="line-white" x1="654" y1="337" x2="670" y2="353"/>

  <!-- side panels -->
  <text class="brand" font-size="70" text-anchor="middle" transform="translate(288,603) rotate(90)">Valmuna</text>
  <text class="brand" font-size="70" text-anchor="middle" transform="translate(1352,603) rotate(-90)">Valmuna</text>

  <!-- front panel 1 -->
  <use href="#front-graphics" y="380"/>
  <text class="brand" x="519" y="485" font-size="60">Valmuna</text>
  <g class="body-text" style="fill:var(--ink)" font-size="21">
    <text x="519" y="520">PIPLERLONGUMINE</text>
    <text x="519" y="545">AND LONG PEPPE</text>
  </g>
  <text class="brand" x="524" y="723" font-size="25" text-anchor="middle">90 Pills</text>
  <g class="body-text ink">
    <text x="1029" y="452" font-size="17">STERILE</text>
    <text x="873" y="665" font-size="15">CONTENTS :</text>
    <text x="873" y="691" font-size="15">One sterile Syringe containing 1.00ml NMB GEL</text>
    <text x="873" y="711" font-size="15">One sterile disposable 27-gauge cannula</text>
    <text x="873" y="742" font-size="18" font-weight="600" letter-spacing="0.4">FOR INTRAOCULAR USE ONLY</text>
    <text x="873" y="770" font-size="18" font-weight="600" letter-spacing="0.4">SINGLE USE ONLY</text>
  </g>
  <text class="condensed" x="1025" y="484">CONTENTS ARE STERILE UNLESS</text>
  <text class="condensed" x="1025" y="508">PACKAGE IS OPENED OR DAMAGED</text>

  <!-- middle band -->
  <rect class="blue" x="379" y="810" width="890" height="136"/>
  <g class="body-text on-blue" font-size="18">
    <text x="473" y="848">Northmere Botanic Ltd.</text>
    <text x="473" y="873">Alder House, Alder Lane, Brackwell, Westshire</text>
    <text x="473" y="897">BK 4 2RT,United Kingdom</text>
    <text x="473" y="921">Website: www.nmb-bio.com&#160;&#160; E-mail: info@nmb-bio.com</text>
    <text x="1012" y="873" font-size="15.5">Mfg. Date :</text>
    <text x="1012" y="909" font-size="15.5">Exp. Date :</text>
  </g>
  <polyline class="line-white" points="961,874 961,862 967,868 973,860 979,866 981,852 984,852 984,874 961,874"/>
  <path class="line-white" d="M961,890 H973 M961,913 H973 M962,891 L972,911 M972,891 L962,911"/>

  <!-- front panel 2 -->
  <use href="#front-graphics" y="947"/>
  <text class="brand" x="519" y="1052" font-size="60">Valmuna</text>
  <g class="body-text" style="fill:var(--ink)" font-size="21">
    <text x="519" y="1088">PIPLERLONGUMINE</text>
    <text x="519" y="1113">AND LONG PEPPE</text>
  </g>
  <text class="brand" x="524" y="1293" font-size="25" text-anchor="middle">90 Pills</text>
  <g class="body-text ink">
    <text x="1029" y="1018" font-size="17">STERILE</text>
    <text x="873" y="1233" font-size="15" font-weight="700">CONTENTS :</text>
    <text x="873" y="1259" font-size="15" font-weight="700">One sterile Syringe containing 1.00ml NMB GEL</text>
    <text x="873" y="1279" font-size="15" font-weight="700">One sterile disposable 27-gauge cannula</text>
    <text x="873" y="1310" font-size="18" font-weight="600" letter-spacing="0.4">FOR INTRAOCULAR USE ONLY</text>
    <text x="873" y="1338" font-size="18" font-weight="600" letter-spacing="0.4">SINGLE USE ONLY</text>
  </g>
  <text class="condensed" x="1025" y="1049">CONTENTS ARE STERILE UNLESS</text>
  <text class="condensed" x="1025" y="1073">PACKAGE IS OPENED OR DAMAGED</text>
</svg>
</body>
</html>
```